Web site for a company that sells Pinball machines

We need a website that is an online shopping experience for a Store that sells pinball machines and accessories. The name of the store is called "Flipside Arcadeworks." The store it self has a showroom, but we would also like to have an Internet e-commerce presence. We pinball machines made by Halvard pinball. You can visit their website and see their current list of machines as well as their website for the machines that we are going to carry in our store. Their website is Halvardpinball.example. I am able to use their machine photos as well as their machine brochure PDF files. I am also able to use their logo on my website two list it as a Halvard Authorized Dealer.
This website design needs to be funky, fun, very technologically oriented and modern. The people buying machines our spending anywhere between $5000 and $15,000 on one machine. These Are high-end buyers who are also usually fairly tech savvy or at least enjoy technology and graphics.
Attachments: I have attached photographs of some of my own machines which may be used in the website. I've also attached some downloaded files from Halvard pinball.example as well as some of their PDF files for brochures. I will carry all of their current models they have listed under games. Not the archived games. I have included one of their machines called Moonbreaker Limited edition in my photograph attachments. The rest of the photos are just random pictures that I have taken myself and maybe used to build the site. Lastly I have attached my logo which I am not super crazy about so I will also be posting a contest to redesign this logo. Tons more of my own pinball photos are available.
I would like for people to be able to purchase machines and accessories from the website, but also inform them to our actual showroom.
Updates
Project Deadline Extended Reason: Hello. We have extended five days due to some complications during the construction of our actual building. We were unable to participate in this web design during this time and so unfortunately were not able give feedback appropriately. We are back on track and will provide feedback to the designers who have designed up until this point. We will still be interested in seeing new submissions, however; this extension will give us a chance to provide feedback and coordinate the website appropriately. Thank you so much for your submissions and your patience!!!!Flipside Arcadeworks Added Friday, April 21, 2017
Target Market(s)
Target market is 16 to 75. Techy individuals to enjoy gaming technology video animation and Vegas style twinkle
Industry/Entity Type
It Company
Coding
Coded - Design and coding required
Number of Pages Required
3 page
Font styles to use
Look and feel
Each slider illustrates characteristics of the customer's brand and the style your logo design should communicate.

```html
<!DOCTYPE html>
<html lang="en">
<head>
<meta charset="utf-8">
<title>Flipside Arcadeworks — Pinball Machines and Accessories</title>
<link href="https://fonts.googleapis.com/css2?family=Montserrat:wght@600;700;800&family=Open+Sans:wght@400;600;700&display=swap" rel="stylesheet">
<style>
:root{
  --navy:#1d2060;
  --red:#d0121b;
  --white:#ffffff;
  --ink:#2b2b33;
  --muted:#6a6a74;
}
*{box-sizing:border-box;margin:0;padding:0}
html,body{width:1200px;height:4401px;overflow:hidden}
body{position:relative;font-family:"Open Sans",Arial,sans-serif;color:var(--ink);
  background:
    radial-gradient(ellipse 300px 160px at 15% 28%,rgba(200,60,60,.35),transparent),
    radial-gradient(ellipse 260px 140px at 85% 33%,rgba(120,60,160,.35),transparent),
    radial-gradient(ellipse 320px 160px at 20% 56%,rgba(210,120,60,.28),transparent),
    radial-gradient(ellipse 300px 160px at 80% 60%,rgba(90,70,150,.32),transparent),
    radial-gradient(ellipse 340px 170px at 30% 76%,rgba(190,70,60,.3),transparent),
    linear-gradient(180deg,#3a1722 0%,#1d0f15 20%,#3b1a1e 40%,#1e1218 60%,#311921 80%,#1a1116 100%)}
.abs{position:absolute}
h2{font-family:"Montserrat",Arial,sans-serif;font-weight:800;text-transform:uppercase;letter-spacing:1px}
.btn{position:absolute;display:flex;align-items:center;justify-content:center;background:var(--red);color:var(--white);
  font-family:"Montserrat",Arial,sans-serif;font-weight:700;font-size:15px;letter-spacing:1px;text-transform:uppercase}

/* header */
.topbar{left:0;top:0;width:1200px;height:88px;background:var(--white)}
.socials{left:78px;top:32px;display:flex;gap:14px}
.socials span{width:17px;height:17px;border-radius:50%;background:#3a3a46;display:block}
.tools{right:78px;top:30px;display:flex;gap:28px}
.nav{left:0;top:88px;width:1200px;height:44px;background:var(--navy);border-bottom:4px solid var(--red)}
.nav a{position:absolute;top:0;line-height:40px;color:var(--white);font-family:"Montserrat",Arial,sans-serif;font-weight:700;font-size:14px;text-decoration:none;text-transform:uppercase}
.brand{left:490px;top:6px;width:220px;height:118px;background:var(--white);border:4px solid var(--navy);border-radius:0 0 60px 60px;
  display:flex;flex-direction:column;align-items:center;justify-content:center;gap:6px}
.brand .dot{width:24px;height:24px;border-radius:50%;background:var(--red)}
.brand .name{font-family:"Montserrat",Arial,sans-serif;font-weight:800;font-size:20px;color:var(--navy);text-transform:uppercase;text-align:center;line-height:1.05}

/* hero */
.hero{left:0;top:132px;width:1200px;height:528px;
  background:
    radial-gradient(ellipse 120px 150px at 64% 20%,rgba(80,200,120,.85),transparent),
    radial-gradient(ellipse 200px 120px at 12% 80%,rgba(160,60,220,.8),transparent),
    radial-gradient(ellipse 180px 120px at 88% 75%,rgba(200,60,200,.6),transparent),
    radial-gradient(ellipse 260px 200px at 35% 30%,rgba(120,120,170,.55),transparent),
    radial-gradient(ellipse 200px 140px at 80% 30%,rgba(230,170,80,.35),transparent),
    linear-gradient(135deg,#2a1848 0%,#4a2a7a 35%,#1b1030 60%,#5a2050 100%)}
.hero-line{left:50%;transform:translateX(-50%);background:rgba(0,0,0,.6);color:var(--white);font-family:"Montserrat",Arial,sans-serif;font-weight:700;font-size:29px;padding:8px 16px;white-space:nowrap;text-transform:uppercase}
.dots{left:585px;top:488px;display:flex;gap:7px}
.dots span{width:10px;height:10px;border-radius:50%;background:var(--white)}

.band{left:0;width:1200px;background:var(--white)}
.section-title{left:0;width:1200px;text-align:center;font-size:36px;color:var(--white)}
.section-title.dark{color:var(--navy)}
.copy{font-size:14px;line-height:23px;color:#444}

/* machine photo stand-ins */
.machine-shot{background:
  radial-gradient(ellipse 22% 30% at 55% 22%,rgba(230,170,90,.9),transparent),
  radial-gradient(ellipse 40% 38% at 45% 60%,rgba(70,80,190,.9),transparent),
  radial-gradient(ellipse 30% 45% at 55% 45%,#2a2040 0%,transparent 100%),
  linear-gradient(180deg,#fafafa 0%,#f2f2f4 100%)}

/* product cards */
.card{top:1153px;width:329px;height:434px;background:var(--white);padding:10px}
.card .shot{height:281px}
.card .info{background:var(--red);height:133px;padding:14px 16px;color:var(--white);position:relative}
.card h3{font-family:"Montserrat",Arial,sans-serif;font-weight:800;font-size:17px;text-transform:uppercase}
.card .price{font-family:"Montserrat",Arial,sans-serif;font-weight:800;font-size:27px;margin-top:2px}
.card .offer{position:absolute;right:14px;top:54px;font-size:12px;text-decoration:underline;font-weight:600}
.card .add,.card .more{position:absolute;top:90px;height:32px;width:140px;display:flex;align-items:center;justify-content:center;
  font-family:"Montserrat",Arial,sans-serif;font-weight:700;font-size:12px;text-transform:uppercase}
.card .add{left:14px;background:var(--navy)}
.card .more{right:14px;border:2px solid var(--white)}

/* gallery & news photo stand-ins */
.photo{box-shadow:0 3px 8px rgba(0,0,0,.3)}
.g1{background:radial-gradient(ellipse 40% 40% at 30% 40%,#e0c050,transparent),radial-gradient(ellipse 50% 50% at 75% 60%,#c83a3a,transparent),linear-gradient(135deg,#3a3a8a,#6a3a6a,#2a2a4a)}
.g2{background:radial-gradient(ellipse 45% 35% at 40% 45%,#e8b040,transparent),radial-gradient(ellipse 40% 40% at 80% 30%,#4aa0c0,transparent),linear-gradient(135deg,#2a1a1a,#7a3a2a,#2a1a2a)}
.g3{background:radial-gradient(ellipse 50% 40% at 50% 40%,#f0c040,transparent),radial-gradient(ellipse 40% 40% at 25% 75%,#d04030,transparent),linear-gradient(135deg,#c06030,#a0304a,#3a2a4a)}
.g4{background:radial-gradient(ellipse 25% 35% at 45% 50%,#e0c070,transparent),linear-gradient(90deg,#5a1010,#a8282a 45%,#6a1414 100%)}
.n1{background:radial-gradient(ellipse 45% 45% at 45% 40%,#f0c040,transparent),radial-gradient(ellipse 40% 45% at 70% 75%,#c03a30,transparent),linear-gradient(135deg,#d09030,#a0303a,#3a2040)}
.n2{background:radial-gradient(ellipse 40% 40% at 50% 40%,#d04a4a,transparent),radial-gradient(ellipse 40% 40% at 30% 80%,#e0b050,transparent),linear-gradient(135deg,#3a2a6a,#7a2a5a,#2a1a3a)}

/* news */
.news-title{font-family:"Montserrat",Arial,sans-serif;font-weight:800;font-size:15px;color:var(--white);text-transform:uppercase;white-space:nowrap}
.news-date{font-family:"Montserrat",Arial,sans-serif;font-weight:700;font-size:12px;color:var(--white);margin:8px 0 6px;display:flex;align-items:center;gap:8px}
.news-copy{font-size:14px;line-height:24px;color:#e6e0e4}

/* features */
.feature{top:3873px;width:329px;height:170px;background:var(--white);border:3px solid var(--navy);text-align:center}
.feature .icon{position:absolute;left:118px;top:-50px;width:88px;height:88px;border-radius:50%;background:var(--white);border:3px solid var(--navy);display:flex;align-items:center;justify-content:center}
.feature h3{margin-top:62px;font-family:"Montserrat",Arial,sans-serif;font-weight:700;font-size:19px;color:var(--red);text-transform:uppercase;white-space:nowrap}
.feature p{font-size:13px;line-height:20px;color:var(--muted);margin:6px 50px 0}
.feature .btn{left:74px;bottom:-22px;width:175px;height:42px}
.feature input{margin:10px auto 0;display:block;width:280px;height:32px;border:1px solid #bbb;text-align:center;font-family:inherit;font-size:13px}

/* footer */
.footer{left:0;top:4137px;width:1200px;height:264px;background:#16121a}
.footer nav a{position:absolute;top:100px;color:var(--white);font-family:"Montserrat",Arial,sans-serif;font-weight:700;font-size:13px;text-transform:uppercase;text-decoration:none}
.copyright{left:76px;top:144px;font-size:12px;color:#a8a2aa}
.pay{right:76px;top:96px;display:flex;gap:8px;align-items:center}
.pay span{width:40px;height:24px;border-radius:3px;background:#e8e8ee;display:block}
.pay span:first-child{width:76px;background:#3b5eb0}
.foot-social{right:76px;top:142px;display:flex;gap:14px}
.foot-social span{width:17px;height:17px;border-radius:50%;background:var(--white);display:block}
</style>
</head>
<body>

<div class="abs topbar">
  <div class="abs socials"><span></span><span></span><span></span><span></span><span></span><span></span></div>
  <div class="abs tools">
    <svg width="20" height="20" viewBox="0 0 20 20" fill="#3a3a46"><circle cx="10" cy="6" r="4.5"/><path d="M1 19c1-6 17-6 18 0z"/></svg>
    <svg width="22" height="20" viewBox="0 0 22 20" fill="#3a3a46"><path d="M0 2h4l3 11h12l3-9H6" fill="none" stroke="#3a3a46" stroke-width="2.4"/><circle cx="9" cy="17" r="2"/><circle cx="17" cy="17" r="2"/></svg>
    <svg width="20" height="20" viewBox="0 0 20 20"><circle cx="8" cy="8" r="6" fill="none" stroke="#3a3a46" stroke-width="2.6"/><path d="M12.5 12.5l6 6" stroke="#3a3a46" stroke-width="3"/></svg>
  </div>
</div>
<nav class="abs nav">
  <a style="left:76px">Home</a><a style="left:176px">About</a><a style="left:286px">Pinball Machines</a>
  <a style="left:778px">Accessories</a><a style="left:934px">Shop</a><a style="left:1032px">Contact Us</a>
</nav>
<div class="abs brand"><span class="dot"></span><span class="name">Flipside<br>Arcadeworks</span></div>

<section class="abs hero" role="img" aria-label="Close-up of a lit pinball playfield with colourful toys and purple lighting"></section>
<div class="abs hero-line" style="top:350px">Welcome to Flipside Arcadeworks</div>
<div class="abs hero-line" style="top:430px">We sells pinball machines and accessories</div>
<div class="abs dots"><span></span><span></span><span></span></div>

<!-- Hot machine -->
<section class="abs band" style="top:660px;height:382px;clip-path:polygon(0 0,100% 0,100% 78%,0 100%)"></section>
<h2 class="abs" style="left:76px;top:712px;font-size:36px;color:var(--navy)">Hot Machine</h2>
<p class="abs copy" style="left:76px;top:772px;width:760px">Aenean a nibh eget turpis vehicula tempus ac sed massa. Vestibulum dolor nulla, ultrices ac tincidunt sed, laoreet non est. Suspendisse lobortis turpis in odio blandit ac interdum lorem euismod. Etiam risus massa, vulputate eu pellentesque et, consectetur a neque. Duis aliquam nibh a dui iaculis viverra id a velit. Vivamus egestas risus in magna varius commodo. Sed semper viverra egestas. Etiam pretium porttitor lectus, vel ornare neque porta volutpat.</p>
<div class="btn" style="left:76px;top:927px;width:176px;height:47px">Read More</div>
<div class="abs machine-shot" role="img" aria-label="Featured pinball machine cabinet with lit backbox" style="left:860px;top:680px;width:255px;height:355px;background:
  radial-gradient(ellipse 22% 18% at 65% 12%,rgba(230,170,90,.95),transparent),
  radial-gradient(ellipse 40% 22% at 50% 55%,rgba(70,90,210,.95),transparent),
  radial-gradient(ellipse 38% 48% at 55% 45%,#2a2448 0%,transparent 100%),#ffffff"></div>

<!-- Machines for sale -->
<h2 class="abs section-title" style="top:1072px">Pinball Machines For Sell</h2>
<article class="abs card" style="left:76px">
  <div class="shot machine-shot" role="img" aria-label="Pinball machine for sale"></div>
  <div class="info"><h3>Game Heading Title</h3><div class="price">$5000</div><span class="offer">Special Offers Available</span><span class="add">Add To Cart</span><span class="more">More Details</span></div>
</article>
<article class="abs card" style="left:437px">
  <div class="shot machine-shot" role="img" aria-label="Pinball machine for sale"></div>
  <div class="info"><h3>Game Heading Title</h3><div class="price">$5000</div><span class="offer">Special Offers Available</span><span class="add">Add To Cart</span><span class="more">More Details</span></div>
</article>
<article class="abs card" style="left:795px">
  <div class="shot machine-shot" role="img" aria-label="Pinball machine for sale"></div>
  <div class="info"><h3>Game Heading Title</h3><div class="price">$5000</div><span class="offer">Special Offers Available</span><span class="add">Add To Cart</span><span class="more">More Details</span></div>
</article>

<!-- Accessories -->
<section class="abs band" style="top:1643px;height:557px;clip-path:polygon(0 0,100% 4%,100% 86%,0 100%)"></section>
<div class="abs" role="img" aria-label="Pinball accessories: shooter assembly, flipper bats, ball and a pinball machine" style="left:65px;top:1716px;width:492px;height:411px;background:
  radial-gradient(ellipse 28% 14% at 40% 10%,rgba(60,70,160,.75),transparent),
  radial-gradient(ellipse 20% 8% at 25% 38%,rgba(40,120,90,.6),transparent),
  radial-gradient(ellipse 16% 16% at 25% 75%,rgba(180,60,140,.6),transparent),
  radial-gradient(ellipse 22% 40% at 72% 62%,rgba(60,50,130,.85),transparent),
  #ffffff"></div>
<h2 class="abs" style="left:613px;top:1780px;font-size:36px;color:var(--navy)">Accessories</h2>
<p class="abs copy" style="left:613px;top:1838px;width:510px">Aenean a nibh eget turpis vehicula tempus ac sed massa. Vestibulum dolor nulla, ultrices ac tincidunt sed, laoreet non est. Suspendisse lobortis turpis in odio blandit ac interdum lorem euismod. Etiam risus massa, vulputate eu pellentesque et, consectetur a neque.<br>Duis aliquam nibh a dui iaculis viverra id a velit.</p>
<div class="btn" style="left:613px;top:1998px;width:179px;height:47px">Visit Store</div>

<!-- Videos -->
<h2 class="abs section-title" style="top:2247px">Videos</h2>
<div class="abs" role="img" aria-label="Video still of a pinball arcade showroom" style="left:255px;top:2324px;width:690px;height:340px;border:6px solid var(--white);background:
  radial-gradient(ellipse 20% 25% at 30% 30%,rgba(220,180,90,.6),transparent),
  radial-gradient(ellipse 25% 25% at 75% 40%,rgba(120,90,170,.6),transparent),
  radial-gradient(ellipse 30% 25% at 40% 80%,rgba(170,70,60,.5),transparent),
  linear-gradient(180deg,#4a3a50,#2a2028)"></div>
<svg class="abs" style="left:556px;top:2450px" width="88" height="88" viewBox="0 0 88 88"><circle cx="44" cy="44" r="38" fill="none" stroke="#fff" stroke-width="7"/><path d="M34 26l28 18-28 18z" fill="#fff"/></svg>
<svg class="abs" style="left:165px;top:2470px" width="36" height="50" viewBox="0 0 36 50"><path d="M30 4L8 25l22 21" fill="none" stroke="#e8e8ee" stroke-width="8"/></svg>
<svg class="abs" style="left:998px;top:2470px" width="36" height="50" viewBox="0 0 36 50"><path d="M6 4l22 21L6 46" fill="none" stroke="#e8e8ee" stroke-width="8"/></svg>

<!-- Gallery -->
<section class="abs band" style="top:2729px;height:498px;clip-path:polygon(0 4%,100% 0,100% 100%,0 90%)"></section>
<h2 class="abs section-title dark" style="top:2806px">Photo Gallery</h2>
<svg class="abs" style="left:26px;top:2995px" width="20" height="30" viewBox="0 0 20 30"><path d="M16 3L5 15l11 12" fill="none" stroke="#ccc" stroke-width="4"/></svg>
<svg class="abs" style="left:1154px;top:2995px" width="20" height="30" viewBox="0 0 20 30"><path d="M4 3l11 12L4 27" fill="none" stroke="#ccc" stroke-width="4"/></svg>
<div class="abs photo g1" role="img" aria-label="Rows of lit pinball machines in a showroom" style="left:76px;top:2919px;width:238px;height:182px"></div>
<div class="abs photo g2" role="img" aria-label="Pinball playfield detail" style="left:346px;top:2919px;width:238px;height:182px"></div>
<div class="abs photo g3" role="img" aria-label="Colourful playfield artwork" style="left:616px;top:2919px;width:238px;height:182px"></div>
<div class="abs photo g4" role="img" aria-label="Coin door on a red cabinet" style="left:886px;top:2919px;width:238px;height:182px"></div>

<!-- News -->
<h2 class="abs section-title" style="top:3267px">News and Events</h2>
<div class="abs photo n1" role="img" aria-label="Pinball playfield with bright artwork" style="left:76px;top:3406px;width:206px;height:188px"></div>
<div class="abs" style="left:311px;top:3400px;width:280px">
  <div class="news-title">Nam Fermentum Vestibulum</div>
  <div class="news-date"><svg width="14" height="14" viewBox="0 0 14 14"><rect x="1" y="2" width="12" height="11" fill="none" stroke="#fff" stroke-width="2"/><path d="M1 5h12" stroke="#fff" stroke-width="2"/></svg>Mar 09, 2017</div>
  <p class="news-copy">Aliquam molestie, mi et imperdiet euismod, dui purus auctor tellus, et interdum lacus lectus et ante. accumsan sollicitudin sapien, mi, vitae suscipit vitae risus.</p>
</div>
<div class="abs photo n2" role="img" aria-label="Pinball playfield seen from above" style="left:619px;top:3406px;width:206px;height:188px"></div>
<div class="abs" style="left:855px;top:3400px;width:280px">
  <div class="news-title">Nam Fermentum Vestibulum</div>
  <div class="news-date"><svg width="14" height="14" viewBox="0 0 14 14"><rect x="1" y="2" width="12" height="11" fill="none" stroke="#fff" stroke-width="2"/><path d="M1 5h12" stroke="#fff" stroke-width="2"/></svg>Mar 09, 2017</div>
  <p class="news-copy">Aliquam molestie, mi et imperdiet euismod, dui purus auctor tellus, et interdum lacus lectus et ante. accumsan sollicitudin sapien, mi, vitae suscipit vitae risus.</p>
</div>

<!-- Features -->
<section class="abs band" style="top:3697px;height:440px;clip-path:polygon(0 8%,100% 0,100% 100%,0 100%)"></section>
<div class="abs feature" style="left:76px">
  <div class="icon"><svg width="44" height="32" viewBox="0 0 44 32" fill="#1d2060"><rect x="0" y="2" width="26" height="20"/><path d="M28 8h9l7 8v6H28z"/><circle cx="9" cy="26" r="5"/><circle cx="35" cy="26" r="5"/></svg></div>
  <h3>Free Shipping</h3><p>Vestibulum ante ipsum primis in faucibus orci luctus</p>
  <div class="btn">Read More</div>
</div>
<div class="abs feature" style="left:437px">
  <div class="icon"><svg width="38" height="38" viewBox="0 0 38 38" fill="#1d2060"><path d="M8 2l7 8-4 5c3 6 7 10 12 12l5-4 8 7-5 6C16 35 3 22 2 8z"/></svg></div>
  <h3>Customer Support</h3><p>Vestibulum ante ipsum primis in faucibus orci luctus</p>
  <div class="btn">Contact Us</div>
</div>
<div class="abs feature" style="left:795px">
  <div class="icon"><svg width="44" height="32" viewBox="0 0 44 32"><rect x="1" y="1" width="42" height="30" fill="#1d2060"/><path d="M2 3l20 15L42 3" fill="none" stroke="#fff" stroke-width="3"/></svg></div>
  <h3>Newsletter Sign Up</h3><input type="text" placeholder="Enter Email Address" aria-label="Email address">
  <div class="btn">Sign Up</div>
</div>

<footer class="abs footer">
  <nav>
    <a style="left:76px">Home</a><a style="left:158px">About</a><a style="left:248px">Pinball Machines</a>
    <a style="left:428px">Accessories</a><a style="left:562px">Shop</a><a style="left:642px">Contact Us</a>
  </nav>
  <div class="abs copyright">Copyright © 2017. Company Name. All Right Reserved</div>
  <div class="abs pay" aria-label="Accepted payment methods"><span></span><span></span><span></span><span></span></div>
  <div class="abs foot-social"><span></span><span></span><span></span><span></span><span></span><span></span></div>
</footer>

</body>
</html>
```